The Vixen Rides Again Line of Sparkling Wine & Spirits

Back info: Tara Rose Whitfield Owner 209-555-0143 1480 E. Harlow Rd, Bldg. 7, & 8, Lodi Ca. 95299
Sparkling Wines & Memorabilia www.thevixenridesagain.example
Ok I have uploaded the winning design. The color that I am after is the Fushia, Raspberry, Red, Matte Satin Matalic Finish. With a 24 Karet Gold color Foil. The Bottle is on the top row and it's the 2nd Bottle in. That is the Color that I want. This is the style of font. Make sure that you put what we're advertising. Good Luck to you all. Warmest regards, Tara
Target Market(s)
21 & up UniSex
Industry/Entity Type
Sparkling Wine and Memorabilia
Contact Information for Business Card
there listed up above.....

```html
<!DOCTYPE html>
<html lang="en">
<head>
<meta charset="utf-8">
<title>The Vixen Rides Again – Business Card</title>
<link href="https://fonts.googleapis.com/css2?family=Arimo:wght@400;700&display=swap" rel="stylesheet">
<style>
  :root {
    --backdrop: #e4e4e4;
    --card-white: #ffffff;
    --fuchsia: #c3136f;
    --fuchsia-bright: #e0198f;
    --fuchsia-deep: #8f1450;
    --gold: #a5752f;
    --ink: #3b3b3b;
    --ink-soft: #4a4a4a;
    --logo-grey: #3a3a3a;
  }
  * { margin: 0; padding: 0; box-sizing: border-box; }
  html, body { width: 1200px; height: 1200px; overflow: hidden; }
  body {
    background: var(--backdrop);
    font-family: "Arimo", Arial, sans-serif;
    position: relative;
  }
  .card {
    position: absolute;
    left: 262px;
    width: 690px;
    height: 393px;
    overflow: hidden;
  }
  .card--front { top: 159px; background: var(--card-white); }
  .card--back {
    top: 653px;
    background: radial-gradient(ellipse 60% 65% at 50% 40%, var(--fuchsia-bright) 0%, #c0157a 50%, var(--fuchsia-deep) 100%);
  }
  .bottle {
    position: absolute;
    border-radius: 10px 10px 8px 8px;
    background: linear-gradient(90deg, #a50f5c 0%, #ee2a96 45%, #c2126f 75%, #8e0d4f 100%);
  }
  .card--front .bottle { left: 61px; top: 53px; width: 88px; height: 295px; }
  .card--back .bottle { left: 102px; top: 65px; width: 75px; height: 256px; }

  .contact {
    position: absolute;
    right: 54px;
    top: 178px;
    text-align: right;
    color: var(--ink);
  }
  .contact__name {
    font-weight: 700;
    font-size: 26px;
    color: var(--fuchsia);
    letter-spacing: 0.2px;
    line-height: 30px;
  }
  .contact__role {
    font-size: 17px;
    color: var(--gold);
    line-height: 20px;
  }
  .contact__address {
    margin-top: 23px;
    font-size: 16px;
    line-height: 21px;
    color: var(--ink-soft);
  }
  .contact__lines { margin-top: 20px; font-size: 16px; line-height: 21px; color: var(--ink-soft); }
  .contact__line { display: flex; justify-content: flex-end; align-items: center; gap: 8px; }
  .contact__line svg { width: 14px; height: 14px; flex: none; }

  .brand {
    position: absolute;
    left: 190px;
    top: 160px;
    width: 370px;
  }
  .brand__name {
    font-weight: 700;
    font-size: 36px;
    color: var(--logo-grey);
    white-space: nowrap;
    line-height: 44px;
  }
  .brand__rule {
    height: 1px;
    margin-top: 8px;
    background: rgba(255,255,255,0.35);
  }
  .brand__tagline {
    margin-top: 10px;
    font-size: 17px;
    color: #ffffff;
    letter-spacing: 1.6px;
    white-space: nowrap;
  }
  .brand__tagline strong { font-weight: 700; }
</style>
</head>
<body>
  <section class="card card--front">
    <div class="bottle" role="img" aria-label="Illustration of a fuchsia sparkling wine bottle with gold foil neck"></div>
    <div class="contact">
      <p class="contact__name">TARA ROSE WHITFIELD</p>
      <p class="contact__role">Owner</p>
      <p class="contact__address">E. Harlow Rd<br>Bldg. 7, &amp; 8, Lodi Ca. 95299</p>
      <div class="contact__lines">
        <p class="contact__line">209-555-0143 1480
          <svg viewBox="0 0 24 24" aria-hidden="true"><path fill="#c3136f" d="M6.6 10.8a15.2 15.2 0 0 0 6.6 6.6l2.2-2.2a1 1 0 0 1 1-.25 11.4 11.4 0 0 0 3.6.57 1 1 0 0 1 1 1V20a1 1 0 0 1-1 1A17 17 0 0 1 3 4a1 1 0 0 1 1-1h3.5a1 1 0 0 1 1 1c0 1.25.2 2.45.57 3.57a1 1 0 0 1-.25 1z"/></svg>
        </p>
        <p class="contact__line">www.thevixenridesagain.example
          <svg viewBox="0 0 24 24" aria-hidden="true"><circle cx="12" cy="12" r="10" fill="#c3136f"/><path d="M12 2a10 10 0 0 1 0 20M2 12h20M12 2c-3 3-3 17 0 20" stroke="#fff" stroke-width="1.5" fill="none"/></svg>
        </p>
      </div>
    </div>
  </section>

  <section class="card card--back">
    <div class="bottle" role="img" aria-label="Illustration of a fuchsia sparkling wine bottle with gold foil neck"></div>
    <div class="brand">
      <p class="brand__name">The Vixen Rides Again</p>
      <div class="brand__rule"></div>
      <p class="brand__tagline">SPARKLING <strong>WINES &amp; MEMORABILIA</strong></p>
    </div>
  </section>
</body>
</html>
```